Varlow's Electrical & Solar - Business Cards

I want my business card to stand out from the rest. I will provide my business name logo and my icon logo to be implemented onto the card.

On the front of the card, can i have the following. Just make it neat & professional please.

Dean Harrop
varlowselectrical@mailbox-example.net
0491 837 562
ABN: 41 269 507 813
License No. 582146K
FREE QUOTES
24/7 Emergency

On the back of the card, can I have "Our Services" and maybe add the V logo on the back in the background or something. Under "Our Services" I want the following:

LED Lighting Upgrades
Switches & Outlets
Smoke Alarms
Switchboard Upgrades
Fault Finding
Rewiring
New Builds
Test & Tagging
All Electrical Maintenance & Repairs

Can you guys add the instagram logo and next to it, put varlows_electrical

Can you guys also add the facebook logo and next to it put Varlow's Electrical & Solar. Make sure the instagram & facebook icon is in either white, green or black.

Also I have put down double sided, not sure why when i save it, it keeps going to single sided. I need my business card double sided.

New Customers

Dean Harrop varlowselectrical@mailbox-example.net 0491 837 562 ABN: 41 269 507 813 License No. 582146K FREE QUOTES 24/7 Emergency

• must be tidy, professional and appealing

```html
<!DOCTYPE html>
<html lang="en">
<head>
<meta charset="utf-8">
<title>Varlow's Electrical &amp; Solar – Business Cards</title>
<link rel="stylesheet" href="https://fonts.googleapis.com/css2?family=Audiowide&family=Poppins:wght@400;500;600&display=swap">
<style>
  :root {
    --bg: #e9e7e3;
    --card: #111111;
    --green: #2fc94c;
    --green-bright: #3fd65a;
    --silver: #b9bec4;
    --white: #ffffff;
    --card-w: 700px;
    --card-h: 400px;
  }
  * { margin: 0; padding: 0; box-sizing: border-box; }
  html, body { width: 1200px; height: 900px; overflow: hidden; background: var(--bg); }
  body { font-family: "Poppins", sans-serif; color: var(--white); position: relative; }

  .card {
    position: absolute;
    width: var(--card-w);
    height: var(--card-h);
    background: var(--card);
    border-radius: 6px;
    overflow: hidden;
    box-shadow: 0 10px 28px rgba(0,0,0,.25);
  }
  .card--back { left: 250px; top: 35px; }
  .card--front { left: 250px; top: 465px; }

  /* Back: services */
  .services { position: absolute; left: 56px; top: 48px; }
  .services__title {
    font-family: "Audiowide", sans-serif;
    color: var(--green);
    font-size: 24px;
    letter-spacing: 1px;
    text-transform: uppercase;
    margin-bottom: 18px;
  }
  .services__list { list-style: none; }
  .services__item {
    display: flex; align-items: center; gap: 12px;
    font-size: 19px; font-weight: 500; line-height: 31px;
  }
  .bolt { width: 10px; height: 18px; flex: none; }

  .brand-mark { position: absolute; display: flex; align-items: center; gap: 14px; }
  .brand-mark__dot { border: 6px solid var(--green); border-radius: 50%; flex: none; }
  .brand-mark__name {
    font-family: "Poppins", sans-serif; font-weight: 600; color: var(--white);
    line-height: 1.15;
  }
  .card--back .brand-mark { right: 46px; top: 110px; flex-direction: column; }
  .card--back .brand-mark__dot { width: 150px; height: 150px; }
  .card--back .brand-mark__name { font-size: 18px; text-align: center; }

  /* Front: contact */
  .contact { position: absolute; left: 54px; top: 52px; }
  .contact__name {
    font-family: "Audiowide", sans-serif; color: var(--green);
    font-size: 28px; letter-spacing: 1px; text-transform: uppercase; margin-bottom: 12px;
  }
  .contact__row { display: flex; align-items: center; gap: 12px; font-size: 18px; line-height: 28px; }
  .contact__row--gap { margin-top: 16px; }
  .icon { width: 18px; height: 18px; flex: none; }
  .social-dot { width: 22px; height: 22px; border: 2px solid var(--green); border-radius: 50%; flex: none; }
  .contact__legal { margin-top: 16px; color: var(--green); font-size: 19px; line-height: 26px; }
  .contact__legal span { color: var(--white); }

  .card--front .brand-mark { right: 40px; top: 62px; flex-direction: column; }
  .card--front .brand-mark__dot { width: 88px; height: 88px; border-width: 5px; }
  .card--front .brand-mark__name { font-size: 20px; text-align: center; }

  .wave { position: absolute; left: 0; bottom: 0; width: 100%; height: 100%; }
  .offer {
    position: absolute; right: 34px; bottom: 60px; text-align: right;
    font-family: "Poppins", sans-serif; color: var(--white); text-transform: uppercase;
  }
  .offer__quotes { font-size: 16px; font-weight: 400; }
  .offer__emergency { font-size: 19px; font-weight: 600; }
</style>
</head>
<body>

<section class="card card--back" aria-label="Card back – our services">
  <div class="services">
    <h2 class="services__title">Our Services</h2>
    <ul class="services__list">
      <li class="services__item"><svg class="bolt" viewBox="0 0 10 18"><path d="M6 0 0 10h4l-2 8 8-11H6l2-7z" fill="#2fc94c"/></svg>LED Lighting Upgrades</li>
      <li class="services__item"><svg class="bolt" viewBox="0 0 10 18"><path d="M6 0 0 10h4l-2 8 8-11H6l2-7z" fill="#2fc94c"/></svg>Switches &amp; Outlets</li>
      <li class="services__item"><svg class="bolt" viewBox="0 0 10 18"><path d="M6 0 0 10h4l-2 8 8-11H6l2-7z" fill="#2fc94c"/></svg>Smoke Alarms</li>
      <li class="services__item"><svg class="bolt" viewBox="0 0 10 18"><path d="M6 0 0 10h4l-2 8 8-11H6l2-7z" fill="#2fc94c"/></svg>Switchboard Upgrades</li>
      <li class="services__item"><svg class="bolt" viewBox="0 0 10 18"><path d="M6 0 0 10h4l-2 8 8-11H6l2-7z" fill="#2fc94c"/></svg>Fault Finding</li>
      <li class="services__item"><svg class="bolt" viewBox="0 0 10 18"><path d="M6 0 0 10h4l-2 8 8-11H6l2-7z" fill="#2fc94c"/></svg>Rewiring</li>
      <li class="services__item"><svg class="bolt" viewBox="0 0 10 18"><path d="M6 0 0 10h4l-2 8 8-11H6l2-7z" fill="#2fc94c"/></svg>New Builds</li>
      <li class="services__item"><svg class="bolt" viewBox="0 0 10 18"><path d="M6 0 0 10h4l-2 8 8-11H6l2-7z" fill="#2fc94c"/></svg>Test &amp; Tagging</li>
      <li class="services__item"><svg class="bolt" viewBox="0 0 10 18"><path d="M6 0 0 10h4l-2 8 8-11H6l2-7z" fill="#2fc94c"/></svg>All Electrical Maintenance &amp; Repairs</li>
    </ul>
  </div>
  <div class="brand-mark">
    <span class="brand-mark__dot"></span>
    <span class="brand-mark__name">Varlow's Electrical<br>&amp; Solar</span>
  </div>
</section>

<section class="card card--front" aria-label="Card front – contact details">
  <svg class="wave" viewBox="0 0 700 400" preserveAspectRatio="none" aria-hidden="true">
    <path d="M0 330 C160 380 300 370 430 300 C520 250 600 210 700 200 L700 400 L0 400 Z" fill="#b9bec4"/>
    <path d="M0 345 C170 400 320 385 450 300 C540 245 610 215 700 205 L700 400 L0 400 Z" fill="#2fc94c"/>
    <path d="M0 330 C160 380 300 370 430 300 C470 280 500 262 530 248 C470 300 380 345 260 350 C160 355 80 345 0 340 Z" fill="#111111" opacity=".0"/>
  </svg>

  <div class="contact">
    <h1 class="contact__name">Dean Harrop</h1>
    <p class="contact__row">
      <svg class="icon" viewBox="0 0 24 24"><path d="M6.6 10.8a15 15 0 0 0 6.6 6.6l2.2-2.2a1 1 0 0 1 1-.25 11.4 11.4 0 0 0 3.6.57 1 1 0 0 1 1 1V20a1 1 0 0 1-1 1A17 17 0 0 1 3 4a1 1 0 0 1 1-1h3.5a1 1 0 0 1 1 1c0 1.25.2 2.45.57 3.6a1 1 0 0 1-.25 1z" fill="#2fc94c"/></svg>
      0491 837 562
    </p>
    <p class="contact__row">
      <svg class="icon" viewBox="0 0 24 24"><rect x="2" y="5" width="20" height="14" rx="1" fill="#2fc94c"/><path d="M2 6l10 7 10-7" stroke="#111" stroke-width="2" fill="none"/></svg>
      varlowselectrical@mailbox-example.net
    </p>
    <p class="contact__row contact__row--gap"><span class="social-dot"></span>varlows_electrical</p>
    <p class="contact__row"><span class="social-dot"></span>Varlow's Electrical &amp; Solar</p>
    <p class="contact__legal">ABN: <span>41 269 507 813</span><br>License No. <span>582146K</span></p>
  </div>

  <div class="brand-mark">
    <span class="brand-mark__dot"></span>
    <span class="brand-mark__name">Varlow's<br>Electrical &amp; Solar</span>
  </div>

  <div class="offer">
    <p class="offer__quotes">Free Quotes</p>
    <p class="offer__emergency">24/7 Emergency</p>
  </div>
</section>

</body>
</html>
```